Prestige Car Bodyshop Business Card

We are a car bodyshop based in the UK. Our customer base is mainly prestige high-value vehicles. I am looking for a classy and stylish business card design for my staff to give out to customers, with their direct email and phone number, as well as our main email and phone number with address details

I am also looking to have a general business card design with just our main company address and contact details, but also have a space to add a manufacturer approval logo (i.e Velmora, Orek, Tovalo etc... logo) in the corner somewhere.

I do not particularly want any outlines or pictures of cars on the card, I would just like a quality high-end look.

Please feel free to get in touch if you have any questions or queries?

Many Thanks

Malcolm

Target Market(s)

Prestige vehicle owners

Industry/Entity Type

Automotive

Contact Information for Business Card

I am looking for a classy and stylish business card design for my staff to give out to customers, with their direct email and phone number, as well as our main email and phone number with address details

Font styles to use
Sans Serif

Colors

Designer to choose colors to be used in the design.

Requirements
Nice to have
• I do not particularly want any outlines or pictures of cars on the card, I would just like a quality high-end look.

```html
<!DOCTYPE html>
<html lang="en">
<head>
<meta charset="utf-8">
<title>Halden Repair Centre – Business Card</title>
<link rel="stylesheet" href="https://fonts.googleapis.com/css2?family=Work+Sans:wght@400;700&display=swap">
<style>
  :root {
    --backdrop: #2b2b2b;
    --card-white: #ffffff;
    --navy: #1f3366;
    --brand-blue: #1a5fa6;
    --blue-light: #1968b3;
    --blue-dark: #1f3565;
    --orange: #f18a2a;
  }
  * { margin: 0; padding: 0; box-sizing: border-box; }
  html, body { width: 1200px; height: 930px; overflow: hidden; }
  body {
    background: var(--backdrop);
    font-family: "Work Sans", Arial, sans-serif;
    position: relative;
  }
  .card {
    position: absolute;
    left: 278px;
    width: 644px;
    height: 368px;
    border-radius: 24px;
  }
  .card-front { top: 76px; background: var(--card-white); color: var(--navy); }
  .card-back {
    top: 486px;
    background: linear-gradient(90deg, var(--blue-light) 0%, var(--brand-blue) 45%, var(--blue-dark) 100%);
    color: var(--card-white);
    display: flex;
    align-items: center;
    justify-content: center;
  }
  .brand {
    display: flex;
    align-items: center;
    gap: 14px;
  }
  .card-front .brand { position: absolute; left: 50px; top: 70px; }
  .brand-mark { display: block; flex: none; }
  .card-front .brand-mark { width: 34px; height: 34px; background: var(--orange); }
  .card-back .brand-mark { width: 46px; height: 46px; background: var(--card-white); }
  .brand-name {
    font-weight: 400;
    line-height: 1;
    letter-spacing: 1px;
    white-space: nowrap;
  }
  .card-front .brand-name { font-size: 26px; color: var(--navy); }
  .card-back .brand-name { font-size: 36px; color: var(--card-white); }
  .staff-details { position: absolute; left: 412px; top: 168px; }
  .staff-name { font-weight: 700; font-size: 25px; letter-spacing: 0.8px; line-height: 1; }
  .staff-role { color: var(--orange); font-size: 15.5px; margin-top: 6px; font-weight: 400; }
  .address { font-size: 16px; line-height: 20px; margin-top: 9px; }
  .contact-list { list-style: none; margin-top: 8px; }
  .contact-list li {
    display: flex; align-items: center;
    font-size: 16px; line-height: 20px;
  }
  .contact-list svg { width: 11px; height: 11px; margin-right: 11px; flex: none; }
</style>
</head>
<body>
  <section class="card card-front">
    <div class="brand">
      <span class="brand-mark"></span>
      <span class="brand-name">HALDEN REPAIR CENTRE</span>
    </div>

    <div class="staff-details">
      <h1 class="staff-name">MARCUS REED</h1>
      <p class="staff-role">Director</p>
      <p class="address">418 Brennard Road<br>Ashford, TX 78102</p>
      <ul class="contact-list">
        <li>
          <svg viewBox="0 0 12 12" aria-hidden="true"><path d="M3 1 L5 3.5 L4 5 Q5.5 7.5 7 8 L8.5 7 L11 9 L9.5 11 Q3 10 1 2.5 Z" fill="#f18a2a"/></svg>
          512 555 0148
        </li>
        <li>
          <svg viewBox="0 0 12 12" aria-hidden="true"><rect x="1" y="2.5" width="10" height="7" fill="none" stroke="#f18a2a" stroke-width="1.3"/><path d="M1 2.5 L6 6.5 L11 2.5" fill="none" stroke="#f18a2a" stroke-width="1.3"/></svg>
          info@haldenrepair.com
        </li>
        <li>
          <svg viewBox="0 0 12 12" aria-hidden="true"><g fill="none" stroke="#f18a2a" stroke-width="1"><circle cx="6" cy="6" r="5"/><ellipse cx="6" cy="6" rx="2.2" ry="5"/><path d="M1 6 H11 M2 3.5 H10 M2 8.5 H10"/></g></svg>
          www.haldenrepair.com
        </li>
      </ul>
    </div>
  </section>

  <section class="card card-back">
    <div class="brand">
      <span class="brand-mark"></span>
      <span class="brand-name">HALDEN REPAIR CENTRE</span>
    </div>
  </section>
</body>
</html>
```